Foldable Flyer Din A4 Charging Infrastructure Real Estate

We need a flyer (size Din A4, folded, see image).
Attached you will find the content with a rough arrangement.
The inner part will contain some Q&A, we have sketched two possible arrangements of the content.
We are looking for a professional design and a good, clean layout.
Maybe you have some ideas how to arrange the content in a smarter way, we are open for suggestions.
The draft contains no images. It would be good to have an explaining image at least on the front of the flyer.
Attached you will find some stock photos we are using on our website, but you can also propose your own images.
If useful, here is our webpage:
https://strom-nest.de/
and the landing page for the offering
https://strom-nest. en/charging-solutions-for-house-management-and-routes/
(this landing page is not professionally designed, so feel free to create a better design for the flyer)
Our target group are real estate managers/facility managers of larger apartment buildings.
The offering is: full-serviced solutions for charging infrastructure for electric cars at the parking lots for residents.
Please do not hesitate to contact me, if you need further information.
Target Market(s)
Professionals in real estate management, facility management
Industry/Entity Type
charging infrastructures for electric cars, focus: appartment buildings
Look and feel
Each slider illustrates characteristics of the customer's brand and the style your logo design should communicate.

```html
<!DOCTYPE html>
<html lang="de">
<head>
<meta charset="utf-8">
<title>strom-nest – Faltflyer Ladeinfrastruktur</title>
<link rel="stylesheet" href="https://fonts.googleapis.com/css2?family=Open+Sans:ital,wght@0,400;0,600;0,700;1,400;1,600&display=swap">
<style>
:root{
  --pink:#e5127f;
  --plum:#3e1a6c;
  --violet:#8a3fc0;
  --violet-light:#9c52d4;
  --navy:#141a25;
  --ink-purple:#8e3ea6;
  --white:#ffffff;
  --muted:#3a4152;
}
*{margin:0;padding:0;box-sizing:border-box}
html,body{width:842px;height:1200px;overflow:hidden;background:#fff}
body{font-family:"Open Sans",Arial,sans-serif;color:var(--white);position:relative}
.panel{position:absolute;overflow:hidden}
.abs{position:absolute}

/* inside, top row */
.problem{left:0;top:0;width:276px;height:595px;background:var(--pink)}
.solution{left:283px;top:0;width:277px;height:595px;background:var(--plum)}
.steps{left:568px;top:0;width:274px;height:595px;background:linear-gradient(180deg,var(--violet),var(--violet-light))}

/* outside, bottom row */
.benefits{left:0;top:605px;width:276px;height:595px;background:var(--plum)}
.contact{left:283px;top:605px;width:277px;height:595px;background:var(--white)}
.cover{left:568px;top:605px;width:274px;height:595px;background:var(--navy)}

.panel-title{font-weight:700;font-size:14px}
.problem .panel-title{color:var(--ink-purple);left:15px;top:22px}
.solution .panel-title{color:var(--pink);left:7px;top:22px}

.question{left:16px;width:160px;font-size:8px;font-weight:600;line-height:1.55}
.dash{height:0;border-top:1px dashed rgba(255,255,255,.75)}
.problem .dash{left:36px;width:234px}
.solution .dash{left:0;width:277px}

.brand-word{font-weight:600;color:var(--white);letter-spacing:.5px}
.problem .brand-word{left:0;width:276px;top:540px;text-align:center;font-size:24px}

.sol{font-size:7.5px;line-height:1.45;width:130px}
.sol.l{left:7px}
.sol.r{left:142px}

.steps-title{left:31px;top:20px;font-size:16px;font-weight:700;line-height:1.75}
.step{left:60px;width:200px;font-size:11.5px;line-height:1.4}
.step h3{font-size:16px;font-weight:600;margin-left:1px;margin-bottom:-1px}
.step p{margin-left:-1px}
.step small{font-size:8.5px}

.intro{left:28px;top:22px;font-size:12px;line-height:1.62;width:220px}
.intro li{list-style:none;padding-left:26px;position:relative}
.intro li svg{position:absolute;left:2px;top:3px}
.highlight{background:var(--pink);font-style:italic;font-size:12.5px;line-height:1.4;padding:6px 4px}

.cta{left:5px;top:17px;width:267px;height:141px;border:1px dashed var(--pink);text-align:center;color:var(--ink-purple);font-family:Arial,Helvetica,sans-serif}
.cta .lead{font-size:12px;margin-top:10px}
.cta .link{font-size:13.5px;margin-top:30px}
.cta .or{font-size:11px;margin-top:6px}
.cta .phone{font-size:13.5px;margin-top:8px}
.about{left:30px;top:178px;width:215px;text-align:center;color:var(--ink-purple);font-family:Arial,Helvetica,sans-serif;font-size:11px;line-height:1.4}
.photo{left:0;top:280px;width:277px;height:258px;background:radial-gradient(circle at 55% 45%,#3f6fe0 0%,#9fb6f0 28%,#e9ecf2 55%,#c9ccd3 100%)}
.imprint{font-size:6px;line-height:1.5;color:var(--ink-purple)}

.cover .small{left:16px;top:14px;width:180px;font-size:8.5px;line-height:1.6}
.cover h2{font-size:15px;font-weight:600;line-height:1.75;left:16px}
.cover .faint{left:20px;width:140px;font-size:9px;line-height:1.75;color:var(--muted)}
.cover .brand-word{left:150px;top:546px;font-size:18px}
</style>
</head>
<body>

<!-- Inside: Problem -->
<section class="panel problem">
  <h2 class="abs panel-title">Problem / Fragestellung</h2>
  <p class="abs question" style="top:46px;width:150px">Ein Bewohner will eine Wallbox – was tun?</p>
  <div class="abs dash" style="top:77px"></div>
  <p class="abs question" style="top:122px;width:160px">Der Stromanschluss reicht nicht, wenn alle Bewohner eine Wallbox wollen!</p>
  <div class="abs dash" style="top:162px"></div>
  <p class="abs question" style="top:196px;width:165px">Sind die Vorabprüfung und der Einbau von Ladeinfrastruktur teuer? Wie überzeugt man die WEG von den Kosten?</p>
  <div class="abs dash" style="top:247px"></div>
  <p class="abs question" style="top:266px;width:130px">Die Bewohner haben keine fest zugeordneten Stellplätze</p>
  <div class="abs dash" style="top:301px"></div>
  <p class="abs question" style="top:320px;left:18px;width:160px">Wer kann helfen, eine professionelle und zukunftsfähige Ladeinfrastruktur zu entwickeln?</p>
  <div class="abs dash" style="top:376px"></div>
  <p class="abs question" style="top:408px;width:155px">Bei uns wurden bereits Wallboxen von einzelnen Mietern installiert, was nun?</p>
  <div class="abs dash" style="top:452px"></div>
  <p class="abs brand-word">strom-nest.de</p>
</section>

<!-- Inside: Solution -->
<section class="panel solution">
  <h2 class="abs panel-title">Der Lösungsansatz von strom-nest</h2>
  <p class="abs sol l" style="top:44px">Mieter/Eigentümer hat nach WoMoG Anspruch auf eine Wallbox.</p>
  <p class="abs sol r" style="top:44px">Die Hausverwaltung darf den Wunsch nicht verhindern, darf aber - und sollte - Vorgaben machen, um eine nachhaltige Gesamtlösung sicherzustellen.</p>
  <div class="abs dash" style="top:106px"></div>
  <p class="abs sol l" style="top:117px">Mit Hilfe des <b>Last-Managements</b> von <b>strom-nest</b> lässt sich die verfügbare Strom-Kapazität intelligent steuern, so dass der</p>
  <p class="abs sol r" style="top:117px">Hausanschluss in der Regel langfristig ausreicht.</p>
  <div class="abs dash" style="top:176px"></div>
  <p class="abs sol l" style="top:187px">Bei der Lösung von <b>strom-nest</b> werden nur aktuell benötigte Wallboxen aufgebaut - <b>erforderliche Investitionen</b></p>
  <p class="abs sol r" style="top:187px"><b>erfolgen schrittweise nach Bedarf</b>.<br><br>Mit dem optionalen Mietmodell entstehen der WEG keine oder nur geringe Kosten, hier können</p>
  <div class="abs dash" style="top:251px"></div>
  <p class="abs sol l" style="top:262px">Der Anschluss an den Wohnungszähler des jeweiligen Mieters/Eigentümers ist <i>nicht</i></p>
  <p class="abs sol r" style="top:262px">notwendig. <b>strom-nest</b> rechnet auf Wunsch mit jedem Mieter direkt dessen Ladestromverbrauch ab.</p>
  <div class="abs dash" style="top:302px"></div>
  <p class="abs sol l" style="top:310px"><b>strom-nest</b> ist Spezialist für Ladeinfrastruktur, und kennt sich neben der speziellen technischen Lösungen auch mit rechtlichen Fragestellungen und Abrechnungslösungen aus.</p>
  <p class="abs sol r" style="top:318px">Neben der Umsetzung unterstützt strom-nest die Hausverwaltungen bei technischen und juristischen Fragen, um zusammen mit der WEG eine optimale Lösung</p>
  <div class="abs dash" style="top:386px"></div>
  <p class="abs sol l" style="top:395px">In vielen Fällen kann Hardware anderer Hersteller in die Abrechnungslösung von <b>strom-nest</b> integriert werden.</p>
</section>

<!-- Inside: Steps -->
<section class="panel steps">
  <h2 class="abs steps-title">Die Schritte zur<br>Ladeinfrastruktur in Ihrem<br>Objekt:</h2>
  <div class="abs step" style="top:130px">
    <h3>1. Erstprüfung</h3>
    <p>• Machbarkeitsprüfung<br>• Abschätzung, Planung nächster Schritte</p>
  </div>
  <div class="abs step" style="top:219px">
    <h3>2. Konzeption</h3>
    <p>•Planung der Anlage<br>•Abstimmung Netzbetreiber<br>•Kostenkalkulation</p>
  </div>
  <div class="abs step" style="top:330px">
    <h3>3. Installation</h3>
    <p>•Installation von Verkabelung und Elektrotechnik<br>•Installation der Wallboxen<br>•Setup der Abrechnungssysteme</p>
  </div>
  <div class="abs step" style="top:456px">
    <h3>4. Betrieb</h3>
    <p>•Technischer Betrieb<br>•Abrechnung<br>•Regelmäßige Wartung <small>(DGUV3)</small><br>•Anmeldung und Verwaltung neuer Nutzer</p>
  </div>
</section>

<!-- Outside: Benefits -->
<section class="panel benefits">
  <div class="abs intro">
    <p>Bieten Sie ihren Bewohnern Lademöglichkeiten für ihre Elektrofahrzeuge –</p>
    <ul>
      <li><svg width="12" height="11" viewBox="0 0 12 11"><path d="M1 6l3.5 3.5L11 1" fill="none" stroke="#e5127f" stroke-width="2"/></svg>einfach,</li>
      <li><svg width="12" height="11" viewBox="0 0 12 11"><path d="M1 6l3.5 3.5L11 1" fill="none" stroke="#e5127f" stroke-width="2"/></svg>unkompliziert und</li>
      <li><svg width="12" height="11" viewBox="0 0 12 11"><path d="M1 6l3.5 3.5L11 1" fill="none" stroke="#e5127f" stroke-width="2"/></svg>zukunftsfähig.</li>
    </ul>
  </div>
  <p class="abs highlight" style="left:15px;top:238px;width:238px">Zukunftsfähig durch flexibles Abrechnungsmodell für verschiedene Einsatzmöglichkeiten.</p>
  <p class="abs highlight" style="left:15px;top:335px;width:238px">Leichter, schneller Einstieg in das Thema, unkomplizierte und professionelle Abwicklung</p>
  <p class="abs highlight" style="left:18px;top:432px;width:242px">Aufbau und Betrieb von Ladelösungen speziell für Hausverwaltungen und WEGs</p>
</section>

<!-- Outside: Contact -->
<section class="panel contact">
  <div class="abs cta">
    <p class="lead">Jetzt Beratungsgespräch anfordern unter:</p>
    <p class="link">https://strom-nest.de/WEG</p>
    <p class="or">oder</p>
    <p class="phone">01234 / 567 89 00</p>
  </div>
  <p class="abs about">Als Anbieter von Full-Service-Lösungen ermöglicht strom-nest eine für Immobilienbesitzer/-verwalter einfache und ausbaubare Lösung, die alle Bereiche abdeckt.</p>
  <div class="abs photo" role="img" aria-label="Foto: Ladestecker eines Elektroautos mit blau leuchtendem Ring"></div>
  <p class="abs imprint" style="left:14px;top:552px">strom-nest GmbH<br>Lindenweg 14<br>80000 Musterstadt</p>
  <p class="abs imprint" style="left:100px;top:564px">HRB 000000<br>Amtsgericht Musterstadt</p>
  <p class="abs imprint" style="left:187px;top:552px">Geschäftsführung: Lena Berger<br><br>Email: <u>info@strom-nest.de</u></p>
</section>

<!-- Outside: Cover -->
<section class="panel cover">
  <p class="abs small">Bauträger und Hausverwaltungen/ WEGs, die einfach zukunftsfähige Ladelösungen für Ihre Stellplätze benötigen</p>
  <h2 class="abs" style="top:82px">Flexible<br>Ladeinfrastrukturen<br>für die Elektromobilität</h2>
  <h2 class="abs" style="top:183px">für Mieter und<br>Eigentümer</h2>
  <h2 class="abs" style="top:258px">einfach, unkompliziert<br>und zukunftsfähig</h2>
  <p class="abs faint" style="top:326px">Hausverwaltungen werden von Mietern und Eigentümern immer öfter konfrontiert mit dem Wunsch nach Lademöglichkeiten für die Bewohner.</p>
  <p class="abs faint" style="top:468px">Zudem verlangt das neue Gebäude-Elektromobilitäts-infrastruktur Gesetz (GEIG) den Ausbau der Ladeinfrastruktur bei der Renovierung der TG.</p>
  <p class="abs brand-word">strom-nest.de</p>
</section>

</body>
</html>
```